Cedar Lantern Roots Gathering Music Conference & Concert Series needs a banner design to welco...

We are looking for a banner to use as a backdrop where people can take pictures and promote the event as they upload to social media. The music conference primarily targets high school students so we are looking for a design that will attract a younger audience. The festival revolves around music appreciation in the US/Mexico border. We like the "Cedar LanternRoots Gathering" trumpet logo on the "5th annual" design attached, but we are open to other designs.
Target Market(s)
ages 15-45
Colors
Designer to choose colors to be used in the design.
Look and feel

```html
<!DOCTYPE html>
<html lang="en">
<head>
<meta charset="utf-8">
<title>Cedar Lantern Roots Gathering – Music Conference &amp; Concert Series</title>
<link rel="stylesheet" href="https://fonts.googleapis.com/css2?family=Oswald:wght@400;600&display=swap">
<style>
  :root {
    --navy-deep: #0f1a5e;
    --navy-mid: #1a2680;
    --violet-glow: #7a5fb8;
    --lilac-glow: #d6c8ee;
    --text-white: #ffffff;
    --page: #e9e9ec;
  }
  * { margin: 0; padding: 0; box-sizing: border-box; }
  html, body {
    width: 1200px;
    height: 673px;
    overflow: hidden;
    background: var(--page);
  }
  .banner {
    position: relative;
    width: 1200px;
    height: 673px;
    overflow: hidden;
    color: var(--text-white);
    font-family: "Oswald", "Arial Narrow", sans-serif;
  }
  .banner__lights {
    position: absolute;
    inset: 0;
    background:
      radial-gradient(ellipse 360px 420px at 140px 160px, rgba(214,200,238,0.55), transparent 70%),
      radial-gradient(ellipse 260px 240px at 380px 70px, rgba(214,200,238,0.40), transparent 70%),
      radial-gradient(ellipse 300px 220px at 700px 40px, rgba(122,95,184,0.40), transparent 70%),
      radial-gradient(ellipse 320px 260px at 1060px 110px, rgba(122,95,184,0.35), transparent 70%),
      radial-gradient(ellipse 260px 300px at 110px 520px, rgba(122,95,184,0.40), transparent 70%),
      linear-gradient(180deg, var(--navy-mid) 0%, var(--navy-deep) 100%);
  }
  .banner__rule {
    position: absolute;
    height: 6px;
    background: var(--text-white);
  }
  .banner__rule--top { left: 392px; width: 636px; top: 213px; }
  .banner__rule--bottom { left: 172px; width: 212px; top: 384px; }
  .banner__mark {
    position: absolute;
    left: 184px;
    top: 246px;
    width: 72px;
    height: 72px;
    border-radius: 50%;
    background: var(--text-white);
  }
  .banner__edition {
    position: absolute;
    left: 407px;
    top: 168px;
    font-size: 40px;
    font-weight: 600;
    letter-spacing: 0.5px;
    line-height: 1;
    text-transform: uppercase;
  }
  .banner__name {
    font-weight: 400;
    line-height: 1;
  }
  .banner__name-main {
    position: absolute;
    left: 270px;
    top: 215px;
    font-size: 122px;
    letter-spacing: 4px;
    text-transform: uppercase;
    white-space: nowrap;
  }
  .banner__name-sub {
    position: absolute;
    left: 396px;
    top: 351px;
    font-size: 78px;
    letter-spacing: 8px;
    white-space: nowrap;
  }
  .banner__tagline {
    position: absolute;
    left: 425px;
    top: 444px;
    font-size: 32px;
    font-weight: 600;
    letter-spacing: 0.5px;
    text-transform: uppercase;
    line-height: 1;
    white-space: nowrap;
  }
</style>
</head>
<body>
  <main class="banner">
    <div class="banner__lights" role="img" aria-label="Strings of glowing bokeh lights hanging down over a deep blue and violet backdrop"></div>
    <span class="banner__rule banner__rule--top"></span>
    <span class="banner__rule banner__rule--bottom"></span>
    <span class="banner__mark"></span>
    <p class="banner__edition">5th Annual</p>
    <h1 class="banner__name">
      <span class="banner__name-main">Cedar Lantern</span>
      <span class="banner__name-sub">Roots Gathering</span>
    </h1>
    <p class="banner__tagline">Music Conference &amp; Concert Series</p>
  </main>
</body>
</html>
```